Website Design - BrightKeyHelpers.com

PLEASE CHECK WORD DOCUMENT ATTACHED FOR WEBSITE FLOW.

Target Market(s)

REAL ESTATE AGENTS ARE THE TARGET MARKET

Industry/Entity Type

Real Estate

Coding

Coded - Design and coding required

Number of Pages Required

4 page

Colors

Designer to choose colors to be used in the design.

Requirements
Must have
• WE LIKE RED LOGO ATTACHED
Nice to have
• PLEASE CHECK WORD DOCUMENT ATTACHED FOR WEBSITE FLOW.
Should not have

```html
<!DOCTYPE html>
<html lang="en">
<head>
<meta charset="utf-8">
<title>BrightKeyHelpers.com</title>
<link href="https://fonts.googleapis.com/css2?family=Poppins:wght@400;500;600;700&family=Great+Vibes&display=swap" rel="stylesheet">
<style>
:root{
  --red:#e3161d;
  --red-dark:#b80f15;
  --navy:#272c86;
  --navy-deep:#1d2370;
  --purple:#7b2b6b;
  --ink:#2a2a35;
  --muted:#6b6b78;
  --paper:#f3f3f5;
  --white:#ffffff;
}
*{box-sizing:border-box;margin:0;padding:0}
html,body{width:1200px;height:4167px;overflow:hidden}
body{font-family:"Poppins",sans-serif;color:var(--ink);background:var(--white);position:relative}
.container{width:736px;margin:0 auto;position:relative}
h2.section-title{font-size:23px;font-weight:700;text-align:center;color:var(--ink)}

/* header */
.site-header{height:83px;background:var(--white);display:flex;align-items:center}
.site-header .container{display:flex;align-items:center;justify-content:space-between}
.brand{display:flex;align-items:center;gap:8px;font-weight:700;font-size:16px;color:var(--red)}
.brand-square{width:14px;height:14px;background:var(--red)}
.main-nav{display:flex;gap:24px;font-size:10px;font-weight:500;color:var(--ink);text-transform:uppercase;margin-left:40px}
.header-phone{display:flex;align-items:center;gap:8px}
.header-phone small{display:block;font-size:9px;color:var(--muted)}
.header-phone strong{font-size:13px;color:var(--red)}

/* hero */
.hero{height:514px;background:linear-gradient(160deg,#5b2a22 0%,#8c2a26 35%,#6a3a2c 65%,#2f2a25 100%);display:flex;flex-direction:column;align-items:center;padding-top:210px;color:var(--white);text-align:center}
.hero h1{font-size:32px;font-weight:700}
.hero p{font-size:17px;font-weight:500;line-height:1.35;margin-top:4px;max-width:560px}

/* options */
.options{height:236px;position:relative;background:var(--paper)}
.options-band{position:absolute;left:0;right:0;top:0;height:170px;background:linear-gradient(180deg,var(--red) 0%,var(--red-dark) 100%)}
.options h2{position:relative;color:var(--white);font-size:22px;font-weight:700;text-align:center;padding-top:48px}
.option-cards{position:absolute;left:236px;top:108px;display:flex;gap:27px}
.option-card{width:227px;height:106px;background:var(--white);border-radius:4px;box-shadow:0 6px 16px rgba(0,0,0,.15);display:flex;flex-direction:column;align-items:center;justify-content:center;gap:6px;border-bottom:5px solid var(--red);text-align:center}
.option-card span{font-size:10px;line-height:1.3;font-weight:700;text-transform:uppercase}

/* how it works */
.how{height:339px;background:var(--paper);padding-top:75px}
.steps{display:flex;justify-content:space-between;align-items:flex-start;margin-top:40px}
.step{width:200px;text-align:center}
.step-num{width:40px;height:40px;border-radius:50%;background:var(--navy);color:var(--white);font-size:12px;font-weight:600;display:flex;align-items:center;justify-content:center;margin:0 auto 16px}
.step p{font-size:10px;line-height:1.5;color:var(--ink)}
.step-arrow{margin-top:12px}

/* service area */
.service{height:153px;background:linear-gradient(90deg,var(--purple),var(--navy));padding-top:30px;text-align:center}
.service h2{color:var(--white);font-size:22px;font-weight:700}
.service-form{display:flex;justify-content:center;margin-top:14px}
.service-form .field{width:376px;height:36px;background:var(--white);font-size:10px;color:#999;text-align:left;padding:11px 12px}
.service-form .btn{width:100px;height:36px;background:var(--red);color:var(--white);font-size:10px;font-weight:700;display:flex;align-items:center;justify-content:center}
.map{height:425px;background:linear-gradient(135deg,#cfe2ec 0%,#e9e6dc 40%,#ece9de 100%)}

/* marketing */
.marketing{height:528px;background:linear-gradient(90deg,#3b2f8f 0%,#553a9b 45%,#b25590 80%,#e07b9d 100%);position:relative;color:var(--white)}
.marketing-photo{position:absolute;right:0;top:0;width:460px;height:528px;background:linear-gradient(90deg,rgba(201,101,150,0) 0%,#c86893 40%,#e1a0b2 100%)}
.marketing .container{padding-top:60px}
.marketing h2{font-size:22px;font-weight:700}
.service-grid{display:grid;grid-template-columns:230px 230px;column-gap:20px;row-gap:28px;margin-top:34px}
.service-item h3{display:flex;align-items:center;gap:10px;font-size:12px;font-weight:600;text-transform:uppercase;margin-bottom:10px}
.service-item p{font-size:10px;line-height:1.55;opacity:.92}

/* packages */
.packages{height:611px;background:var(--paper);padding-top:64px}
.package-row{display:flex;gap:12px;justify-content:center;margin-top:28px}
.package{width:139px;height:452px;background:var(--white);box-shadow:0 4px 14px rgba(0,0,0,.1);text-align:center;padding:0 12px}
.package-head{height:46px;display:flex;align-items:center;justify-content:center;font-size:12px;font-weight:600;margin:0 -12px}
.package.featured .package-head{background:var(--red);color:var(--white)}
.price{width:50px;height:50px;border-radius:50%;background:var(--red);color:var(--white);font-size:16px;font-weight:700;display:flex;align-items:center;justify-content:center;margin:6px auto 18px}
.package.featured .price{background:var(--navy)}
.package ul{list-style:none;text-align:left}
.package li{font-size:9px;line-height:1.45;color:var(--muted);padding-left:14px;position:relative;margin-bottom:12px}
.package li::before{content:"";position:absolute;left:2px;top:3px;width:5px;height:8px;border:solid var(--red);border-width:0 2px 2px 0;transform:rotate(45deg)}
.package .btn{display:flex;align-items:center;justify-content:center;height:34px;background:var(--navy);color:var(--white);font-size:9px;font-weight:600;margin:14px 6px 16px;line-height:1.2;padding:0 6px}
.package.featured .btn{background:var(--red)}
.package .fine{font-size:8px;line-height:1.45;color:var(--muted)}

/* faq */
.faq{height:431px;background:linear-gradient(180deg,var(--purple) 0%,var(--navy) 100%);padding-top:56px}
.faq h2{color:var(--white);font-size:22px;font-weight:700;text-align:center}
.faq-cols{display:flex;justify-content:space-between;margin-top:34px}
.faq-col{width:353px}
.faq-item{height:36px;background:var(--white);display:flex;align-items:center;justify-content:space-between;padding:0 12px;font-size:10px;font-weight:500;margin-bottom:8px}
.faq-item b{font-size:15px;font-weight:500;color:var(--muted)}
.faq-item.open{background:var(--red);color:var(--white);margin-bottom:0}
.faq-item.open b{color:var(--white)}
.faq-body{background:var(--white);font-size:9.5px;line-height:1.55;padding:10px 12px;color:var(--muted);margin-bottom:8px}

/* testimonials */
.testimonials{height:472px;background:var(--white);padding-top:64px}
.quotes{display:flex;justify-content:space-between;margin-top:34px}
.quote{width:340px;text-align:center}
.quote-text{position:relative;padding:0 30px;font-size:10px;line-height:1.6;color:var(--muted)}
.quote-text::before,.quote-text::after{position:absolute;font-size:44px;font-weight:700;color:var(--red);line-height:1}
.quote-text::before{content:"\201C";left:0;top:-6px}
.quote-text::after{content:"\201D";right:0;bottom:-30px}
.avatar{width:52px;height:52px;border-radius:50%;background:linear-gradient(135deg,#d8d4d0,#a79e96);margin:40px auto 10px;border:3px solid var(--paper)}
.signature{font-family:"Great Vibes",cursive;font-size:26px;color:var(--ink)}
.dots{display:flex;gap:6px;justify-content:center;margin-top:30px}
.dots span{width:8px;height:8px;border-radius:50%;background:#ddd}
.dots span.active{background:var(--red)}

/* newsletter + footer */
.newsletter{position:absolute;left:436px;top:3789px;width:328px;height:44px;border-radius:22px;background:var(--red);color:var(--white);font-size:11px;font-weight:700;display:flex;align-items:center;justify-content:center;gap:10px;z-index:2;text-transform:uppercase}
.site-footer{height:347px;background:var(--navy-deep);color:var(--white);padding-top:60px}
.footer-cols{display:flex;justify-content:space-between}
.footer-col h4{font-size:10px;font-weight:700;text-transform:uppercase;margin-bottom:12px}
.footer-col p,.footer-col li{font-size:9px;line-height:1.7;opacity:.85;list-style:none}
.col-about{width:200px}.col-contact{width:170px}.col-links{width:120px}.col-form{width:150px}
.socials{display:flex;gap:6px;margin-top:12px}
.socials span{width:20px;height:20px;border-radius:50%;border:1px solid rgba(255,255,255,.8)}
.footer-input{height:18px;background:var(--white);margin-bottom:6px;font-size:8px;color:#999;padding:3px 6px}
.footer-input.tall{height:40px}
.footer-btn{height:22px;background:var(--red);font-size:8.5px;font-weight:700;display:flex;align-items:center;justify-content:center;text-transform:uppercase}
.copyright{height:28px;background:#151a5c;color:rgba(255,255,255,.8);font-size:9px}
.copyright .container{display:flex;justify-content:space-between;align-items:center;height:28px}
</style>
</head>
<body>

<header class="site-header">
  <div class="container">
    <div class="brand"><span class="brand-square"></span>BrightKeyHelpers</div>
    <nav class="main-nav"><span>How it works</span><span>Service area</span><span>Pricing</span><span>About us</span><span>FAQ</span></nav>
    <div class="header-phone">
      <svg width="20" height="20" viewBox="0 0 24 24"><path d="M6.6 10.8a15 15 0 0 0 6.6 6.6l2.2-2.2a1 1 0 0 1 1-.25 11.4 11.4 0 0 0 3.6.57 1 1 0 0 1 1 1V20a1 1 0 0 1-1 1A17 17 0 0 1 3 4a1 1 0 0 1 1-1h3.5a1 1 0 0 1 1 1c0 1.25.2 2.45.57 3.57a1 1 0 0 1-.25 1z" fill="#e3161d"/></svg>
      <div><small>Call Or Text Us</small><strong>1-555-014-2290</strong></div>
    </div>
  </div>
</header>

<section class="hero" role="img" aria-label="Photo of a red open house arrow sign on a front lawn before a brick home">
  <h1>Helping agents save time and money.</h1>
  <p>We place signs and boost foot traffic to your open houses using proven marketing techniques.</p>
</section>

<section class="options">
  <div class="options-band"></div>
  <h2>Choose The Option Below That Best Describes You</h2>
  <div class="option-cards">
    <div class="option-card">
      <svg width="26" height="24" viewBox="0 0 26 24"><rect x="3" y="4" width="20" height="19" fill="none" stroke="#e3161d" stroke-width="2"/><rect x="7" y="8" width="3" height="3" fill="#e3161d"/><rect x="12" y="8" width="3" height="3" fill="#e3161d"/><rect x="17" y="8" width="2" height="3" fill="#e3161d"/><rect x="7" y="14" width="3" height="3" fill="#e3161d"/><rect x="16" y="14" width="3" height="3" fill="#e3161d"/><rect x="11" y="16" width="4" height="7" fill="#e3161d"/></svg>
      <span>I'm a<br>Full on brokerage</span>
    </div>
    <div class="option-card">
      <svg width="30" height="24" viewBox="0 0 30 24"><circle cx="15" cy="7" r="4" fill="#e3161d"/><circle cx="6" cy="9" r="3" fill="#e3161d"/><circle cx="24" cy="9" r="3" fill="#e3161d"/><path d="M8 22a7 7 0 0 1 14 0z" fill="#e3161d"/><path d="M1 22a5 5 0 0 1 8-4v4zM29 22a5 5 0 0 0-8-4v4z" fill="#e3161d"/></svg>
      <span>I'm an<br>Ind. broker with a team</span>
    </div>
    <div class="option-card">
      <svg width="24" height="26" viewBox="0 0 24 26"><rect x="4" y="1" width="2" height="24" fill="#e3161d"/><rect x="2" y="24" width="8" height="2" fill="#e3161d"/><rect x="6" y="4" width="16" height="2" fill="#e3161d"/><rect x="9" y="7" width="12" height="9" fill="none" stroke="#e3161d" stroke-width="2"/></svg>
      <span>I need<br>Sign placement ASAP</span>
    </div>
  </div>
</section>

<section class="how">
  <div class="container">
    <h2 class="section-title">How It Works</h2>
    <div class="steps">
      <div class="step"><div class="step-num">01</div><p>We boost foot traffic to your open house using proven marketing channels: Social Ads, SMS notifications, voice broadcasts and email notifications</p></div>
      <svg class="step-arrow" width="40" height="12" viewBox="0 0 40 12"><path d="M0 6h37M32 1l5 5-5 5" fill="none" stroke="#2a2a35" stroke-width="1.3"/></svg>
      <div class="step"><div class="step-num">02</div><p>We place open house signs strategically in the surrounding area</p></div>
      <svg class="step-arrow" width="40" height="12" viewBox="0 0 40 12"><path d="M0 6h37M32 1l5 5-5 5" fill="none" stroke="#2a2a35" stroke-width="1.3"/></svg>
      <div class="step"><div class="step-num">03</div><p>Store custom signs for you if needed</p></div>
    </div>
  </div>
</section>

<section class="service">
  <h2>Service Area</h2>
  <div class="service-form"><div class="field">Enter Your Open House Address</div><div class="btn">SUBMIT</div></div>
</section>
<div class="map" role="img" aria-label="Road map of the coastal service area with cities and highways"></div>

<section class="marketing">
  <div class="marketing-photo" role="img" aria-label="Photo of a smiling woman shouting into a megaphone"></div>
  <div class="container">
    <h2>Marketing Services</h2>
    <div class="service-grid">
      <div class="service-item">
        <h3><svg width="22" height="22" viewBox="0 0 22 22"><circle cx="11" cy="11" r="10" fill="none" stroke="#fff" stroke-width="1.5"/><path d="M6 8h10v6H10l-3 2v-2H6z" fill="#fff"/></svg>SMS</h3>
        <p>We will send a Text Message to all the people that live in the surrounding area of your Open House to let them know there is a home for sale in their neighborhood and to let anyone that they may know looking to purchase a new home to come check it out!</p>
      </div>
      <div class="service-item">
        <h3><svg width="22" height="22" viewBox="0 0 22 22"><rect x="2" y="5" width="18" height="12" fill="none" stroke="#fff" stroke-width="1.5"/><path d="M2 5l9 7 9-7" fill="none" stroke="#fff" stroke-width="1.5"/></svg>Email</h3>
        <p>We will send an Email Message to all the people that live in the surrounding area of your Open House to let them know there is a home for sale in their neighborhood and to let anyone that they may know looking to purchase a new home to come check it out!</p>
      </div>
      <div class="service-item">
        <h3><svg width="22" height="22" viewBox="0 0 22 22"><rect x="2" y="2" width="18" height="18" fill="none" stroke="#fff" stroke-width="1.5"/></svg>Social Ads</h3>
        <p>We will place a social media ad in the news feeds of all the people that live in the surrounding area of your Open House to let them know there is a home for sale in their neighborhood and to let anyone that they may know looking to purchase a new home to come check it out!</p>
      </div>
      <div class="service-item">
        <h3><svg width="22" height="22" viewBox="0 0 22 22"><rect x="8" y="2" width="6" height="11" rx="3" fill="#fff"/><path d="M5 10a6 6 0 0 0 12 0M11 16v4M7 20h8" fill="none" stroke="#fff" stroke-width="1.5"/></svg>Voice Broadcast</h3>
        <p>We will send a voice broadcast to all the people that live in the surrounding area of your Open House to let them know there is a home for sale in their neighborhood and to let anyone that they may know looking to purchase a new home to come check it out!</p>
      </div>
    </div>
  </div>
</section>

<section class="packages">
  <h2 class="section-title">Choose Your Package</h2>
  <div class="package-row">
    <div class="package"><div class="package-head">5 SIGNS</div><div class="price">$49</div><ul><li>Place signs strategically in best areas according to where the open house is located</li><li>Pick up the signs after the open house</li><li>Store custom signs for you if needed</li></ul><div class="btn">SIGN UP</div><p class="fine">Sign Up For A Subscription And Get Three Marketing Services For Free</p></div>
    <div class="package"><div class="package-head">10 SIGNS</div><div class="price">$59</div><ul><li>Place signs strategically in best areas according to where the open house is located</li><li>Pick up the signs after the open house</li><li>Store custom signs for you if needed</li></ul><div class="btn">SIGN UP</div><p class="fine">Sign Up For A Subscription And Get Three Marketing Services For Free</p></div>
    <div class="package featured"><div class="package-head">15 SIGNS</div><div class="price">$69</div><ul><li>Place signs strategically in best areas according to where the open house is located</li><li>Pick up the signs after the open house</li><li>Store custom signs for you if needed</li></ul><div class="btn">SIGN UP</div><p class="fine">Sign Up For A Subscription And Get Three Marketing Services For Free</p></div>
    <div class="package"><div class="package-head">20 SIGNS</div><div class="price">$79</div><ul><li>Place signs strategically in best areas according to where the open house is located</li><li>Pick up the signs after the open house</li><li>Store custom signs for you if needed</li></ul><div class="btn">SIGN UP</div><p class="fine">Sign Up For A Subscription And Get Three Marketing Services For Free</p></div>
    <div class="package"><div class="package-head">25+ SIGNS</div><div class="price">$$</div><ul><li>Place signs strategically in best areas according to where the open house is located</li><li>Pick up the signs after the open house</li><li>Store custom signs for you if needed</li></ul><div class="btn">CLICK HERE TO CREATE CUSTOM PKG</div><p class="fine">Sign Up For A Subscription And Get Three Marketing Services For Free</p></div>
  </div>
</section>

<section class="faq">
  <h2>Frequently Asked Questions</h2>
  <div class="container faq-cols">
    <div class="faq-col">
      <div class="faq-item">Vestibulum sed felis a ante suscipit auctor<b>+</b></div>
      <div class="faq-item">Sed ullamcorper augue ut facilisis condimentum<b>+</b></div>
      <div class="faq-item">Curabitur at ligula sed velit feugiat pellentesque<b>+</b></div>
      <div class="faq-item">Nam vitae velit non augue ultricies laoreet<b>+</b></div>
    </div>
    <div class="faq-col">
      <div class="faq-item">Curabitur at ligula sed velit feugiat pellentesque<b>+</b></div>
      <div class="faq-item open">Lorem ipsum used in various languages for layouts<b>&minus;</b></div>
      <div class="faq-body">In publishing and graphic design, lorem ipsum is a placeholder text commonly used to demonstrate the visual form of a document. In publishing and graphic design, lorem ipsum is a placeholder text commonly used to demonstrate the visual form of a document.</div>
      <div class="faq-item">Sed ullamcorper augue ut facilisis condimentum<b>+</b></div>
      <div class="faq-item">Nam vitae velit non augue ultricies laoreet<b>+</b></div>
    </div>
  </div>
</section>

<section class="testimonials">
  <div class="container">
    <h2 class="section-title">Clients Testimonials</h2>
    <div class="quotes">
      <div class="quote">
        <p class="quote-text">In publishing and graphic design, lorem ipsum is a placeholder text commonly used to demonstrate the visual form of a document. In publishing and graphic design, lorem ipsum is a placeholder text used to demonstrate the visual form of a document.</p>
        <div class="avatar" role="img" aria-label="Client portrait"></div>
        <div class="signature">Marisol Grant</div>
      </div>
      <div class="quote">
        <p class="quote-text">In publishing and graphic design, lorem ipsum is a placeholder text commonly used to demonstrate the visual form of a document. In publishing and graphic design, lorem ipsum is a placeholder text used to demonstrate the visual form of a document.</p>
        <div class="avatar" role="img" aria-label="Client portrait"></div>
        <div class="signature">Theo Ramsay</div>
      </div>
    </div>
    <div class="dots"><span></span><span></span><span class="active"></span><span></span><span></span></div>
  </div>
</section>

<div class="newsletter">
  <svg width="16" height="12" viewBox="0 0 16 12"><rect x="1" y="1" width="14" height="10" fill="none" stroke="#fff" stroke-width="1.4"/><path d="M1 1l7 5 7-5" fill="none" stroke="#fff" stroke-width="1.4"/></svg>
  Subscribe to our newsletter
</div>

<footer class="site-footer">
  <div class="container footer-cols">
    <div class="footer-col col-about">
      <h4>About BrightKey Helpers</h4>
      <p>Owned and operated by a highly experienced Homeowner, Expert Marketer and a Top Realtor, we help agents leverage their time and skills to increase production at an affordable price with impeccable support!</p>
      <div class="socials"><span></span><span></span><span></span><span></span><span></span></div>
    </div>
    <div class="footer-col col-contact">
      <h4>Contact Information</h4>
      <p>4520 Maple Grove Drive<br>Suite 210, Amity, TX 75000</p>
      <p style="margin-top:8px">Call Or Text Us:<br>1-555-014-2290</p>
      <p style="margin-top:8px">Email Us:<br>info@brightkeyhelpers.com</p>
    </div>
    <div class="footer-col col-links">
      <h4>Quick Links</h4>
      <ul><li>How it Works</li><li>Service Area</li><li>Pricing</li><li>About Us</li><li>FAQ</li></ul>
    </div>
    <div class="footer-col col-form">
      <h4>Contact Us Right Now</h4>
      <div class="footer-input">Name</div>
      <div class="footer-input">Email</div>
      <div class="footer-input">Phone</div>
      <div class="footer-input tall">Message</div>
      <div class="footer-btn">Send a message</div>
    </div>
  </div>
</footer>
<div class="copyright">
  <div class="container"><span>Copyright © 2018 BrightKey Helpers. All rights reserved.</span><span>Terms of Use | Privacy | Sitemap</span></div>
</div>

</body>
</html>
```